Business Card Design

We need a new business card design for a company based in Larkmont, TX. We provide business consulting services in the information technology / services space. We like variations of the color blue, aqua, black, light tan, and white. Would like "cool" tones. The design should clearly communicate professionalism. Think outside the box - we don't want something "typical". Our company name is "Vantrell Advisory, LLC".
Updates

Thank you all for your submissions. We have seen some very creative and inspired designs. We have made a decision and will be moving forward with that design. Appreciate all of the hard work.

Industry/Entity Type

Information Technology

Contact Information for Business Card

Denise Harlow Trumbey
482 West Maple Ridge Dr.
Larkmont, TX 76185

```html
<!DOCTYPE html>
<html lang="en">
<head>
<meta charset="utf-8">
<title>Vantrell Advisory, LLC – Business Card</title>
<link rel="stylesheet" href="https://fonts.googleapis.com/css2?family=Arimo:wght@400;700&display=swap">
<style>
  :root {
    --page-bg: #e4e2dc;
    --card-cream: #f4f1ad;
    --card-cream-soft: #f7f5c4;
    --header-dark: #151512;
    --brand-tan: #b8b27a;
    --ink: #111111;
    --ink-soft: #3a3a32;
    --band-green: #5aa877;
    --band-green-light: #77bf8a;
    --band-blue: #2f4ea3;
    --band-blue-light: #4a6cc0;
  }
  html, body {
    margin: 0;
    padding: 0;
    width: 1200px;
    height: 800px;
    overflow: hidden;
    background: var(--page-bg);
  }
  .canvas {
    position: relative;
    width: 1200px;
    height: 800px;
  }
  .card {
    position: absolute;
    left: 100px;
    top: 114px;
    width: 1000px;
    height: 572px;
    overflow: hidden;
    background: linear-gradient(to bottom,
      var(--header-dark) 0%,
      #5b5a45 9%,
      #c9c68c 19%,
      var(--card-cream) 27%,
      var(--card-cream-soft) 100%);
    box-shadow: 0 10px 30px rgba(0,0,0,0.18);
    font-family: "Arimo", Arial, sans-serif;
  }
  .card__bands {
    position: absolute;
    inset: 0;
  }
  .brand {
    position: absolute;
    left: 56px;
    top: 30px;
    margin: 0;
    font-size: 22px;
    font-weight: 400;
    letter-spacing: 4px;
    text-transform: uppercase;
    color: var(--brand-tan);
  }
  .contact-name {
    position: absolute;
    left: 0;
    right: 0;
    top: 212px;
    margin: 0;
    text-align: center;
    font-size: 30px;
    font-weight: 700;
    color: var(--ink);
  }
  .contact-address {
    position: absolute;
    left: 40px;
    top: 352px;
    margin: 0;
    font-size: 17px;
    font-weight: 400;
    font-style: normal;
    color: var(--ink-soft);
  }
</style>
</head>
<body>
<main class="canvas">
  <section class="card" aria-label="Business card">
    <svg class="card__bands" viewBox="0 0 1000 572" width="1000" height="572" aria-hidden="true">
      <defs>
        <linearGradient id="green-band" x1="0" y1="0" x2="0" y2="1">
          <stop offset="0" stop-color="#77bf8a"/>
          <stop offset="1" stop-color="#5aa877"/>
        </linearGradient>
        <linearGradient id="blue-band" x1="0" y1="0" x2="1" y2="0">
          <stop offset="0" stop-color="#2f4ea3"/>
          <stop offset="1" stop-color="#4a6cc0"/>
        </linearGradient>
      </defs>
      <polygon class="band band--blue" points="580,468 940,468 1000,480 1000,512 880,548 650,512" fill="url(#blue-band)"/>
      <polygon class="band band--green" points="320,400 1000,400 1000,468 440,468" fill="url(#green-band)"/>
    </svg>
    <h1 class="brand">Vantrell Advisory, LLC</h1>
    <p class="contact-name">Denise Harlow Trumbey</p>
    <address class="contact-address">482 West Maple Ridge Dr.&nbsp; Larkmont, TX 76185</address>
  </section>
</main>
</body>
</html>
```